LOGO AND 3 PACKAGES.IN 4 different strengths

I need '3' designs for the packages attached.
Im launching a new electronic cigarette BRAND in Australia.
VORTEK
a logo will be a great advantage also to suit VORTEK...
My company name is Pelmora.
The designs need to be retail orientated and focused on getting the attention of the public in a eye catching way that separates our product from any other.
The designs must have all the information back and front and to the print scale.
Easy to read with a nice layout.
I've included some examples to speed the process up.
Who ever wins this will have the opportunity for a lot more work with me.
The company is looking to expand and grow significantly in the coming year.
We look to be the biggest in our arena.
Website to be - www.vortekvapes.example

Reason: Waiting on final designs and judges its tight.

http://www.regfiles.example/Details/R4471Q00835

For information on packaging design please see this attachment for Lettering and requirements.
I hope this helps.
Nicotine falls into Schedule 7 .
If you want to win other customers over I suggest you know as much as possible .
If your not interested then no worries.

You have until today to wrap it up people thanks.

Lyle

Target Market(s)

SMOKERS
PEOPLE LOOKING TO QUIT
Convenience stores major and minor

Industry/Entity Type

Electronic

Logo Text

VORTEK

Logo styles of interest
Emblem Logo
Pictorial/Combination Logo
Abstract Logo
Character Logo
Wordmark Logo
Font styles to use
Sans Serif
Decorative
Other font styles liked:
• VORTEK or CUSTOM TEXT to SUIT

Colors
00a98f
33a7d7
fbee3e
ec1f27
e34197
f37123

Requirements
Must have
• THE ALTERNATIVE SMOKING DEVICE
THE MOST TRUSTED BRAND
THE DISPOSABLE pack and the Rechargeable cartomisers 1 cartomizer = 2packs of cigarettes
400 puffs
VORTEK IS AN AUSTRALIAN BRAND
MUST BE +18
REFF TO EXAMPLES FOR OTHER MUST HAVES PRODUCT CERTIFICATION
SGS ROHS ECT..
Each package has a different strength of nicotine zero%-1.8%-and 2.4%
In 4 different flavors menthol-special blend Tobacco-New Vanilla-and Coffee/Mocha
For now.
Nice to have
• UV silver, green's blue's and reds
I like the carbon look and the metal grating backgrounds.
Slogan
"LIVE FOR IT"
QUALITY BRAND 100% GUARANTEED
Should not have
• NOTHING IMPLYING THAT THIS IS A HEALTHIER OPTION THEN SMOKING
ANY other types of packages PLEASE stick to the templates
WORD Disposable, WORD REchargeable and WORD CArtomizers.

```html
<!DOCTYPE html>
<html lang="en">
<head>
<meta charset="UTF-8">
<title>Vortek Pack – Front and Side Panels</title>
<link rel="stylesheet" href="https://fonts.googleapis.com/css2?family=Anton&family=Oswald:wght@300;400;500&family=Arimo:wght@400&display=swap">
<style>
  :root {
    --page: #ffffff;
    --pack-black: #111111;
    --pack-edge: #2a2a2a;
    --brand-red: #ec1f27;
    --detail-grey: #bdbdbd;
    --badge-grey: #3a3a3a;
    --lotus-pink: #e34197;
    --lotus-orange: #f37123;
    --lotus-violet: #8e3c9e;
  }
  html, body {
    margin: 0;
    padding: 0;
    width: 1200px;
    height: 899px;
    overflow: hidden;
    background: var(--page);
  }
  .canvas {
    position: relative;
    width: 1200px;
    height: 899px;
  }

  /* Side panel */
  .pack-side {
    position: absolute;
    left: 280px;
    top: 110px;
    width: 150px;
    height: 690px;
    background: var(--pack-black);
    border-right: 2px solid var(--pack-edge);
  }
  .side-claim {
    position: absolute;
    left: 50%;
    top: 380px;
    margin: 0;
    transform: translate(-50%, -50%) rotate(-90deg);
    white-space: nowrap;
    font-family: "Oswald", sans-serif;
    font-weight: 400;
    font-size: 36px;
    color: var(--brand-red);
  }
  .side-dots {
    position: absolute;
    left: 63px;
    top: 630px;
    width: 24px;
    height: 46px;
  }

  /* Front panel */
  .pack-front {
    position: absolute;
    left: 432px;
    top: 110px;
    width: 500px;
    height: 690px;
    background: var(--pack-black);
    text-align: center;
  }
  .strength-line {
    position: absolute;
    left: 0;
    right: 0;
    top: 48px;
    margin: 0;
    font-family: "Oswald", sans-serif;
    font-weight: 500;
    font-size: 26px;
    line-height: 1;
    letter-spacing: 1px;
    color: var(--brand-red);
  }
  .flavour-line {
    position: absolute;
    left: 0;
    right: 0;
    top: 86px;
    margin: 0;
    font-family: "Oswald", sans-serif;
    font-weight: 300;
    font-size: 20px;
    line-height: 1;
    letter-spacing: 1px;
    color: var(--detail-grey);
  }
  .brand-name {
    position: absolute;
    left: 0;
    right: 0;
    top: 150px;
    margin: 0;
    font-family: "Anton", sans-serif;
    font-weight: 400;
    font-size: 96px;
    line-height: 1.05;
    color: var(--brand-red);
  }
  .tagline {
    position: absolute;
    left: 0;
    right: 0;
    top: 268px;
    margin: 0;
    font-family: "Oswald", sans-serif;
    font-weight: 300;
    font-size: 40px;
    line-height: 1;
    color: var(--brand-red);
  }
  .lotus-emblem {
    position: absolute;
    left: 170px;
    top: 330px;
    width: 160px;
    height: 90px;
  }
  .slogan {
    position: absolute;
    left: 0;
    right: 0;
    top: 440px;
    margin: 0;
    font-family: "Arimo", sans-serif;
    font-size: 68px;
    line-height: 1.1;
    color: var(--brand-red);
  }
  .pack-details {
    position: absolute;
    left: 30px;
    right: 30px;
    top: 545px;
    margin: 0;
    font-family: "Oswald", sans-serif;
    font-weight: 400;
    font-size: 20px;
    line-height: 1.4;
    letter-spacing: 0.5px;
    color: var(--detail-grey);
  }
  .pack-details strong {
    font-weight: 500;
    color: var(--brand-red);
  }
  .cert-badges {
    position: absolute;
    left: 30px;
    bottom: 24px;
    display: flex;
    gap: 10px;
  }
  .cert-badge {
    width: 34px;
    height: 34px;
    border-radius: 50%;
    background: var(--badge-grey);
  }
  .web-address {
    position: absolute;
    right: 30px;
    bottom: 30px;
    margin: 0;
    font-family: "Oswald", sans-serif;
    font-weight: 400;
    font-size: 18px;
    line-height: 1;
    color: var(--detail-grey);
  }
</style>
</head>
<body>
<main class="canvas">
  <section class="pack-side">
    <p class="side-claim">We are the most trusted brand</p>
    <svg class="side-dots" viewBox="0 0 24 46" aria-hidden="true">
      <circle cx="12" cy="8" r="6" fill="#444444"/>
      <circle cx="12" cy="36" r="6" fill="#444444"/>
    </svg>
  </section>

  <section class="pack-front">
    <p class="strength-line">NICOTINE 1.8%</p>
    <p class="flavour-line">SPECIAL BLEND TOBACCO</p>

    <h1 class="brand-name">Vortek</h1>
    <p class="tagline">The new way of smoking</p>

    <svg class="lotus-emblem" viewBox="0 0 160 90" role="img" aria-label="Lotus flower illustration in pink, violet and orange">
      <defs>
        <radialGradient id="lotusTone" cx="50%" cy="55%" r="60%">
          <stop offset="0%" stop-color="#f37123"/>
          <stop offset="55%" stop-color="#e34197"/>
          <stop offset="100%" stop-color="#8e3c9e"/>
        </radialGradient>
      </defs>
      <ellipse cx="80" cy="45" rx="80" ry="45" fill="url(#lotusTone)"/>
    </svg>

    <p class="slogan">live for it</p>

    <p class="pack-details">
      <strong>400 PUFFS</strong> · 1 = 2 PACKS OF CIGARETTES<br>
      MUST BE 18+ · VORTEK IS AN AUSTRALIAN BRAND
    </p>

    <div class="cert-badges" role="img" aria-label="Product certification marks">
      <span class="cert-badge"></span>
      <span class="cert-badge"></span>
      <span class="cert-badge"></span>
    </div>
    <p class="web-address">www.vortekvapes.example</p>
  </section>
</main>
</body>
</html>
```